Morvek Menu

Hi there,
My restaurant called "Morvek" means Spice in hebrew.
We are middle eastern restaurant that specialist in dips,salads and hot bread baked on the spot and charcoal grilled meat skewers
The restaurant is pretty casual and the atmosphere is nice and customers feels like home.
on www.morvek.com.au you can see photos of the restaurant and the food.
ill add up the menus that i would like to be design please and the logo that is on the front of the shop is been add up
thank you

Target Market(s)

The regulars of the restaurant is jewish/israelis

Industry/Entity Type

Restaurant

```html
<!DOCTYPE html>
<html lang="en">
<head>
<meta charset="utf-8">
<title>Morvek – Lunch Menu</title>
<link rel="stylesheet" href="https://fonts.googleapis.com/css2?family=Crimson+Pro:wght@400&family=Cedarville+Cursive&family=Kalam:wght@400;700&family=Archivo+Narrow:wght@700&family=Libre+Baskerville:ital,wght@1,400;1,700&display=swap">
<style>
:root{
  --canvas:#ffffff;
  --board-top:#2e2e2e;
  --board-bottom:#050505;
  --chalk:#f4f4f4;
  --gold:#f6b72a;
  --item:#f4b62c;
  --rule:#9a9a9a;
  --label:#3a3a3a;
  --phone-blue:#2f8fd6;
}
*{margin:0;padding:0;box-sizing:border-box}
html,body{width:1200px;height:1000px;overflow:hidden;background:var(--canvas)}
.canvas{position:relative;width:1200px;height:1000px}
.page{position:absolute;top:74px;width:560px;height:792px;overflow:hidden;
  background:radial-gradient(ellipse at 40% 10%,var(--board-top) 0%,#161616 55%,var(--board-bottom) 100%);color:var(--chalk)}
.page--3{left:34px}
.page--4{left:613px}
.abs{position:absolute}
.brand{left:78px;top:14px;font-family:"Crimson Pro",serif;font-size:82px;line-height:1;color:var(--chalk);letter-spacing:1px}
.ornament{left:71px;top:106px;width:247px;height:82px;border-top:2px solid var(--chalk);border-bottom:2px solid var(--chalk);
  background:linear-gradient(180deg,#1b1b1b,#2a2a2a)}
.ornament div{position:absolute;inset:8px 0;background:repeating-linear-gradient(90deg,#cfcfcf 0 2px,#1c1c1c 2px 9px);opacity:.55}
.contact{left:344px;top:92px;font-family:"Libre Baskerville",serif;font-style:italic;font-weight:700;color:var(--chalk)}
.contact .tag{font-size:7.5px;line-height:10px}
.contact .line{display:flex;align-items:center;gap:5px;font-size:12px;height:24px}
.contact .dot{width:17px;height:17px;border-radius:50%;background:var(--phone-blue);display:flex;align-items:center;justify-content:center}
.contact .sq{width:15px;height:15px;background:var(--phone-blue)}
.contact .hours{font-size:7.5px;line-height:10px;margin-top:6px}
.script{font-family:"Cedarville Cursive",cursive;font-size:56px;line-height:64px;color:var(--chalk)}
.photo{left:416px;width:115px}
.course{left:64px;top:298px;font-family:"Kalam",cursive;font-weight:700;font-size:44px;line-height:50px;color:var(--gold)}
.heading{font-family:"Kalam",cursive;font-weight:400;font-size:24px;line-height:28px;color:var(--chalk)}
.note{font-family:"Libre Baskerville",serif;font-style:italic;font-size:8.5px;line-height:12px;color:var(--chalk)}
.list{font-family:"Archivo Narrow",sans-serif;font-weight:700;font-size:11.5px;color:var(--item)}
.row{display:flex;height:16px;line-height:16px;white-space:nowrap}
.rule{height:0;border-top:1px dashed var(--rule)}
.vrule{width:0;border-left:1px dashed var(--rule)}
.p3-name{width:285px}
.p4-name{width:143px}
.p4-price{width:70px}
.p4-name2{width:95px}
.kids-name{width:145px}
.sides-name{width:94px}
.cols{display:flex}
.cols .col{width:166px}
.page-label{position:absolute;top:916px;width:200px;text-align:center;font-family:"Archivo Narrow",sans-serif;font-weight:700;font-size:24px;color:var(--label)}
</style>
</head>
<body>
<div class="canvas">

  <section class="page page--3">
    <div class="abs brand">Morvek</div>
    <div class="abs ornament" role="img" aria-label="Geometric star pattern band with red, blue and yellow centres"><div></div></div>
    <div class="abs contact">
      <p class="tag">Always Connected with us</p>
      <p class="line"><span class="dot"><svg width="10" height="10" viewBox="0 0 10 10"><path d="M2 1 L4 1 L4.6 3 L3.4 3.8 Q4.4 5.8 6.2 6.6 L7 5.4 L9 6 L9 8 Q5.5 9 2.6 6 Q0.6 3.6 2 1Z" fill="#fff"/></svg></span>95550142</p>
      <p class="line"><span class="sq"></span>Morvek</p>
      <p class="hours">Sunday - Friday 11:30-9:30<br>Saturday from 5:30-10.00<br>412 Larkmere Road, Ashby North</p>
    </div>
    <div class="abs script" style="left:63px;top:220px">Lunch Menu</div>

    <div class="abs photo" style="top:273px;height:111px;background:radial-gradient(circle at 50% 55%,#c98a55,#6a5a4a 60%,#2a2a2a)" role="img" aria-label="Tasting platter of small dips and salads"></div>
    <div class="abs photo" style="top:394px;height:110px;background:linear-gradient(180deg,#3a3a3a,#d8c3a0 45%,#b89a72 75%,#eee)" role="img" aria-label="Stack of freshly baked flatbread"></div>
    <div class="abs photo" style="top:516px;height:113px;background:radial-gradient(circle at 50% 65%,#d9b676,#a86a3c 60%,#3a3a3a)" role="img" aria-label="Hummus plate being scooped with bread"></div>
    <div class="abs photo" style="top:639px;height:113px;background:radial-gradient(circle at 50% 65%,#9fb36a,#c9503a 45%,#f0f0f0 70%,#3a3a3a)" role="img" aria-label="Bowl of chopped Israeli salad"></div>

    <div class="abs course">Entrée</div>

    <div class="abs heading" style="left:64px;top:357px">Starters</div>
    <div class="abs list" style="left:64px;top:386px">
      <div class="row"><span class="p3-name">Falafel Balls</span><span>$5.00</span></div>
      <div class="row"><span class="p3-name">Moroccan Beef Cigars (3 per serve)</span><span>$11.00</span></div>
      <div class="row"><span class="p3-name">Fried Cauliflower</span><span>$8.00</span></div>
      <div class="row"><span class="p3-name">Pan Fried Mushrooms and Onions</span><span>$8.00</span></div>
      <div class="row"><span class="p3-name">Lamb Kibbeh &amp; Pinenuts (3 per serve)</span><span>$7.50</span></div>
    </div>
    <div class="abs rule" style="left:64px;top:480px;width:307px"></div>

    <div class="abs heading" style="left:64px;top:493px">Hummus Plate</div>
    <div class="abs note" style="left:64px;top:520px">Served with 1 Laffa and MixedPickles</div>
    <div class="abs list" style="left:64px;top:536px">
      <div class="row"><span class="p3-name">Masabacha – served with Tahini and whole Chickpeas</span><span>$11.90</span></div>
      <div class="row"><span class="p3-name">Ful– served with warm, crushed Fava Beans</span><span>$14.90</span></div>
      <div class="row"><span class="p3-name">Mushroom– served with Pan Fried Mushrooms</span><span>$14.90</span></div>
      <div class="row"><span class="p3-name">Basar– served with Mince Lamb &amp; Pine nuts</span><span>$16.50</span></div>
    </div>
    <div class="abs rule" style="left:64px;top:614px;width:307px"></div>

    <div class="abs heading" style="left:64px;top:625px">Salads &amp; Dips Platter</div>
    <div class="abs note" style="left:64px;top:653px">3 Choices &amp; Laffa for $15.00 or 6 choices &amp; 2 Laffa for $28.00</div>
    <div class="abs list cols" style="left:64px;top:673px">
      <div class="col">
        <div class="row">Hummus</div><div class="row">Tahini</div><div class="row">Baba Ganoush</div><div class="row">White Cabbage</div><div class="row">Chatzilim (Fried Eggplant)</div>
      </div>
      <div class="col">
        <div class="row">Liora's Corn Salad</div><div class="row">Moroccan Carrot</div><div class="row">Roasted Beetroot</div><div class="row">Turkish Dip</div><div class="row">Mixed Pickles</div>
      </div>
    </div>
  </section>

  <section class="page page--4">
    <div class="abs brand">Morvek</div>
    <div class="abs ornament" role="img" aria-label="Geometric star pattern band with red, blue and yellow centres"><div></div></div>
    <div class="abs contact">
      <p class="tag">Always Connected with us</p>
      <p class="line"><span class="dot"><svg width="10" height="10" viewBox="0 0 10 10"><path d="M2 1 L4 1 L4.6 3 L3.4 3.8 Q4.4 5.8 6.2 6.6 L7 5.4 L9 6 L9 8 Q5.5 9 2.6 6 Q0.6 3.6 2 1Z" fill="#fff"/></svg></span>95550142</p>
      <p class="line"><span class="sq"></span>Morvek</p>
      <p class="hours">Sunday - Friday 11:30-9:30<br>Saturday from 5:30-10.00<br>412 Larkmere Road, Ashby North</p>
    </div>
    <div class="abs script" style="left:49px;top:220px">Lunch Menu</div>

    <div class="abs photo" style="left:413px;top:256px;height:113px;background:radial-gradient(circle at 55% 60%,#c8c04a,#8a7a2a 55%,#3a2a1a)" role="img" aria-label="Bowl of green olives and pickled peppers"></div>
    <div class="abs photo" style="left:413px;top:381px;height:115px;background:radial-gradient(circle at 50% 55%,#e0b060,#a8642c 55%,#3a2a1a)" role="img" aria-label="Golden fried falafel balls"></div>
    <div class="abs photo" style="left:413px;top:508px;height:113px;background:radial-gradient(circle at 60% 40%,#e0702c,#8a8a6a 55%,#dcdcdc)" role="img" aria-label="Moroccan carrot salad and dips"></div>
    <div class="abs photo" style="left:413px;top:633px;height:113px;background:radial-gradient(circle at 50% 75%,#ffb030,#c0401a 45%,#2a1a10)" role="img" aria-label="Meat skewers over glowing charcoal"></div>

    <div class="abs heading" style="left:50px;top:304px">Israeli Lunch Tasting Plates</div>
    <div class="abs note" style="left:50px;top:332px">All tasting plates include a Chef's Selection of 4 Salads &amp; Dips and Laffa</div>
    <div class="abs list" style="left:50px;top:351px">
      <div class="row"><span class="p4-name">Chicken Shashlik Plate</span><span class="p4-price">$10</span><span class="p4-name2">Chicken Liver Plate</span><span>$9.50</span></div>
      <div class="row"><span class="p4-name">Lamb Shashlik Plate</span><span class="p4-price">$11.50</span><span class="p4-name2">Schnitzel Plate</span><span>$11.00</span></div>
      <div class="row"><span class="p4-name">Kebab (Kofta) Shashlik Plate</span><span class="p4-price">$10.00</span><span class="p4-name2">Falafel Plate</span><span></span></div>
    </div>
    <div class="abs rule" style="left:50px;top:408px;width:340px"></div>

    <div class="abs heading" style="left:50px;top:415px">Wraps</div>
    <div class="abs note" style="left:50px;top:441px">Fresh Laffa wrap withHummus, Tahini, Israeli salad &amp; Mixed Pickles (Chilli optional)</div>
    <div class="abs list" style="left:50px;top:455px">
      <div class="row"><span class="p4-name">Falafel wrap</span><span class="p4-price">$12</span><span class="p4-name2">Kofta wrap</span><span>$14</span></div>
      <div class="row"><span class="p4-name">Chicken wrap</span><span class="p4-price">$14</span><span class="p4-name2">Lamb wrap</span><span>$15</span></div>
      <div class="row"><span class="p4-name">Schnitzel wrap</span><span class="p4-price">$14</span></div>
    </div>
    <div class="abs rule" style="left:50px;top:515px;width:340px"></div>

    <div class="abs heading" style="left:50px;top:529px">Individual Shashlik</div>
    <div class="abs note" style="left:50px;top:555px">(1 Per serve)</div>
    <div class="abs list" style="left:50px;top:570px">
      <div class="row"><span class="p4-name">Chicken Shashlik</span><span class="p4-price">$10</span><span class="p4-name2">Chicken Liver</span><span>$9.50</span></div>
      <div class="row"><span class="p4-name">Lamb Shashlik</span><span class="p4-price">$11.50</span><span class="p4-name2">Schnitzel</span><span>$11.00</span></div>
      <div class="row"><span class="p4-name">Kebab (Kofta) Shashlik</span><span class="p4-price">$10.00</span></div>
    </div>
    <div class="abs rule" style="left:50px;top:630px;width:340px"></div>

    <div class="abs heading" style="left:50px;top:641px">Kids Meal</div>
    <div class="abs note" style="left:50px;top:667px">(10 and under only)</div>
    <div class="abs list" style="left:50px;top:683px">
      <div class="row">Schnitzel plate with chips and</div>
      <div class="row"><span class="kids-name">Israeli Salad</span><span>$10.00</span></div>
      <div class="row">Falafel Plate with chips and</div>
      <div class="row"><span class="kids-name">Israeli Salad</span><span>$9.00</span></div>
    </div>
    <div class="abs vrule" style="left:244px;top:644px;height:102px"></div>

    <div class="abs heading" style="left:263px;top:639px">Sides</div>
    <div class="abs list" style="left:263px;top:666px">
      <div class="row"><span class="sides-name">Israeli Salad</span><span>$10.00</span></div>
      <div class="row"><span class="sides-name">Chips</span><span>$8.00</span></div>
      <div class="row"><span class="sides-name">Laffa</span><span>$2.50</span></div>
      <div class="row"><span class="sides-name">Mix Pickles</span><span>$6.00</span></div>
    </div>
  </section>

  <div class="page-label" style="left:216px">Page 3</div>
  <div class="page-label" style="left:830px">Page 4</div>
</div>
</body>
</html>
```